依頼詳細
【Tobiraのサービス特徴はこの3つ!】
●無料で請求書管理
請求書の作成・PDFダウンロードなどの機能はずっと無料でご利用になれます。顧客の数や、請求書の枚数に制限はありません。さらに有料プランなら見積り機能も使えます
●あんしんの印刷・郵送システム
Tobiraでは安全なドキュメントセンターで印刷、封入、封かん、発送を行なっています。それぞれの作業は機械が行うため請求書をの中身を人が見るということや人為的なミスはありません。詳しくはこちら
●どこでも請求書の作成・管理ができる
専用画面からログインすれば、書き方がわからなくてもテンプレートの必要事項を埋めるだけで出張先や自宅、iPad、スマートフォンなどからいつでも作成・編集できます。

---------------------------------------------------------------------------------

今回は、2種類のデザインを採用させていただきます。
1件10万円で、2種類の募集となりますので、
ドド~ンと総額20万円のキャンペーンとなります。
記載項目
■ 希望するデザイン
フリーランスのエンジニアさん、デザイナーさんが使いたくなる、オシャレで格好いい請求書の、オリジナルのデザインをご提案ください。

また、以下内容は請求書面として必要な事項となりますので必ず記載ください。
(現状の請求書のデータをアップロードしておりますので参照・活用ください)
・請求年月日
・請求先名称
・請求元(名前、住所、TEL、FAX、メールアドレス)
・請求元印影画像
・請求金額合計
・請求明細(20行、小計、消費税、合計金額)
・備考欄(3行)
・振込口座欄(1行)
希望イメージ
• +5 0 +5
• シンプル
複雑
• 単色
カラフル
• 暗い
明るい
• 日常
高級
• 遊び心
厳粛
• 未来的
伝統的
• 女性的
男性的
希望する色
色の指定はございません
納品ファイル
• イラストレーター形式 (.ai)
• フォトショップ形式 (.psd)
補足説明
■ 納品ファイルの希望
Illustrator形式、Photoshop形式、Fireworks形式
(最大容量は1024kbとしてそれ以下で作ってください)
依頼公開後の追記内容
■ 選んだ理由

bluewhistlerさんの作品は、どの業種でも使いやすく受け取り手も安心できるデザインということで選ばせて頂きました

もう一点は(http://www.kumoshi-hub.jp/work/proposal/5830417)になります。(現在システムの都合で当選にできていません)
k-atelierさんの作品は請求書のかっちりした感じに少し遊びを加えた感じのバランスがよく、採用しました。

■ 提案者全員のお礼・コメント

これほど多くの応募をいただけるとは思っておらずとても驚くとともに、感謝の気持でいっぱいです。

請求書のデザインということで、単純にデザイン性だけでは判断できず、どれも素敵な作品ばかりだったので選定には本当に時間がかかりました。

今回の当選作品以外にもTobira賞として10点ほど買取のオファーを出させて頂きます。どうぞよろしくおねがいします。

この度は本当にご応募ありがとうございました。

```html
<!DOCTYPE html>
<html lang="ja">
<head>
<meta charset="utf-8">
<title>御請求書</title>
<link href="https://fonts.googleapis.com/css2?family=Noto+Sans+JP:wght@400;500;700&display=swap" rel="stylesheet">
<style>
:root{
  --ink:#231815;
  --dark:#2b2422;
  --band:#e6e6e6;
  --band-soft:#f1f1f1;
  --rule:#9a9a9a;
  --paper:#ffffff;
  --seal:#e2474b;
  --seal-fill:#fbe3e3;
  --muted:#6b6b6b;
}
*{box-sizing:border-box;margin:0;padding:0}
html,body{width:846px;height:1200px;overflow:hidden;background:var(--paper)}
body{font-family:"Noto Sans JP",sans-serif;color:var(--ink);position:relative}
.abs{position:absolute}
.doc-title{left:80px;top:80px;width:212px;height:58px;background:var(--dark);color:#fff;
  font-size:26px;font-weight:500;letter-spacing:6px;display:flex;align-items:center;justify-content:center}
.issue{left:648px;top:26px;border-left:2px solid var(--ink);padding-left:12px;height:44px;font-size:15px;line-height:20px;color:var(--muted)}
.top-rule{left:648px;top:72px;width:170px;height:1px;background:var(--rule)}
.client{left:80px;top:158px;width:680px;font-size:26px;font-weight:700;display:flex;align-items:baseline;gap:12px}
.client .mark{font-size:22px}
.client .hon{font-size:15px;font-weight:400}
.client-rule{left:80px;top:210px;width:380px;height:2px;background:var(--ink)}
.issuer{left:480px;top:228px;width:340px;font-size:13px;line-height:20px}
.issuer .name{font-size:15px;font-weight:700;border-bottom:1px solid var(--ink);padding-bottom:3px;margin-bottom:6px;width:200px;white-space:nowrap}
.issuer .address{padding-left:24px}
.issuer .contact{margin-top:12px;white-space:nowrap}
.seal{left:708px;top:228px;width:100px;height:100px;border:3px solid var(--seal);background:var(--seal-fill)}
.greeting{left:80px;top:284px;font-size:14px}
.amount{left:80px;top:340px;width:300px;height:46px;border:2px solid var(--ink);display:flex}
.amount .label{background:var(--dark);color:#fff;font-size:13px;width:104px;display:flex;align-items:center;justify-content:center}
.amount .value{flex:1;display:flex;align-items:center;justify-content:center;font-size:24px;font-weight:500;letter-spacing:1px}
.items{left:80px;top:398px;width:738px;border-collapse:collapse;font-size:13px;border-top:2px solid var(--ink)}
.items th{background:#d9d9d9;font-weight:500;height:28px;text-align:left;padding-left:10px;border-right:1px solid var(--rule)}
.items th.c{text-align:center;padding:0}
.items td{height:23px;border-right:1px solid var(--rule);padding:0 8px;line-height:23px}
.items tbody tr:nth-child(odd) td{background:var(--band)}
.items tbody tr:nth-child(even) td{background:var(--paper)}
.items td.c{text-align:center}
.items td.r{text-align:right}
.items th:last-child,.items td:last-child{border-right:none}
.bank-head{left:80px;top:912px;width:420px;height:22px;background:var(--dark);color:#fff;font-size:13px;padding-left:8px;line-height:22px}
.bank{left:92px;top:940px;font-size:13px;line-height:18px}
.totals{left:516px;top:903px;width:302px;border-collapse:collapse;font-size:13px}
.totals td{height:24px;border-bottom:1px solid var(--rule);padding:0 8px}
.totals td.k{text-align:center;width:140px;background:var(--band-soft)}
.totals td.v{text-align:right}
.totals tr.grand td{font-weight:700;border-top:2px solid var(--ink);border-bottom:2px solid var(--ink)}
.note{left:80px;top:998px;font-size:12px;color:var(--muted)}
.remarks{left:80px;top:1022px;width:738px;height:146px;border:1px solid var(--rule);padding:8px 12px;font-size:13px}
.remarks .line{border-bottom:1px dotted var(--rule);height:32px}
</style>
</head>
<body>
<div class="abs issue">発行年月日<br>2013/05/11</div>
<div class="abs top-rule"></div>
<div class="abs doc-title">御請求書</div>

<div class="abs client"><span class="mark">▶</span>サンプル 株式会社<span class="hon">様</span></div>
<div class="abs client-rule"></div>

<div class="abs issuer">
  <div class="name">ミナトデザイン株式会社</div>
  <div class="address">〒150-0042<br>東京都渋谷区<br>宇田川町4丁目2番8号<br>コモレビル2F</div>
  <div class="contact">TEL : 03-5812-4470 / FAX : 03-5812-4471<br>E-mail : office@minato-design.jp</div>
</div>
<div class="abs seal" role="img" aria-label="請求元の角印の印影"></div>

<div class="abs greeting">下記の通り、御請求申し上げます。</div>
<div class="abs amount"><div class="label">ご請求金額</div><div class="value">¥ 84,000－</div></div>

<table class="abs items">
  <colgroup><col style="width:340px"><col style="width:107px"><col style="width:119px"><col style="width:92px"><col style="width:80px"></colgroup>
  <thead><tr><th>品番・品名</th><th class="c">数量</th><th class="c">単位</th><th class="c">単価(¥)</th><th class="c">金額(¥)</th></tr></thead>
  <tbody>
    <tr><td>デザイン</td><td class="c">1</td><td class="c">式</td><td class="r">20,000</td><td class="r">20,000</td></tr>
    <tr><td>企画・取材費用</td><td class="c">1</td><td class="c">式</td><td class="r">60,000</td><td class="r">60,000</td></tr>
    <tr><td></td><td></td><td></td><td></td><td></td></tr><tr><td></td><td></td><td></td><td></td><td></td></tr>
    <tr><td></td><td></td><td></td><td></td><td></td></tr><tr><td></td><td></td><td></td><td></td><td></td></tr>
    <tr><td></td><td></td><td></td><td></td><td></td></tr><tr><td></td><td></td><td></td><td></td><td></td></tr>
    <tr><td></td><td></td><td></td><td></td><td></td></tr><tr><td></td><td></td><td></td><td></td><td></td></tr>
    <tr><td></td><td></td><td></td><td></td><td></td></tr><tr><td></td><td></td><td></td><td></td><td></td></tr>
    <tr><td></td><td></td><td></td><td></td><td></td></tr><tr><td></td><td></td><td></td><td></td><td></td></tr>
    <tr><td></td><td></td><td></td><td></td><td></td></tr><tr><td></td><td></td><td></td><td></td><td></td></tr>
    <tr><td></td><td></td><td></td><td></td><td></td></tr><tr><td></td><td></td><td></td><td></td><td></td></tr>
    <tr><td></td><td></td><td></td><td></td><td></td></tr><tr><td></td><td></td><td></td><td></td><td></td></tr>
  </tbody>
</table>

<div class="abs bank-head">▼お振込み先</div>
<div class="abs bank">さくら平和銀行　中央支店<br>普通口座　01234567<br>サンプル（カ</div>

<table class="abs totals">
  <tr><td class="k">小　計</td><td class="v">80,000</td></tr>
  <tr><td class="k">消費税(5%)</td><td class="v">4,000</td></tr>
  <tr class="grand"><td class="k">合計金額</td><td class="v">84,000</td></tr>
</table>

<div class="abs note">※お振込み手数料は、ご負担お願い致します。</div>
<div class="abs remarks">
  備考）
  <div class="line"></div><div class="line"></div><div class="line"></div>
</div>
</body>
</html>
```